Wordpress Web Design Project for Upmarket Trendy Modern Travel Agency

We are a independent travel agency that does not offer online bookings (at this stage). We offer quality service and this needs to be reflected somehow in the design i.e. good old fashioned service.

Looking for wordpress Design for Travel Site

Company Name Voyage Harbour

www.voyageharbour-example.com.au

Looking for something outside the box and not from layout lagoon.

Something uniquely different !

Reason: Just have not see the right design.

Target Market(s)

Everyone

Industry/Entity Type

Travel

Requirements
Must have
• 1. Booking form
2. Seo friendly layout
3. Everything should be managed from wordpress admin

```html
<!DOCTYPE html>
<html lang="en">
<head>
<meta charset="utf-8">
<title>Voyage Harbour</title>
<link rel="stylesheet" href="https://fonts.googleapis.com/css2?family=Roboto+Condensed:wght@300;400&family=Roboto+Slab:wght@300;400&family=PT+Serif&display=swap">
<style>
:root{
  --blue:#1ab0e3;
  --blue-dark:#1489b5;
  --navy:#0f2c45;
  --ink:#222;
  --grey-band:#eeeeee;
  --footer:#b4b4b4;
}
*{margin:0;padding:0;box-sizing:border-box}
html,body{width:1084px;height:1200px;overflow:hidden}
body{position:relative;background:#fff;font-family:"PT Serif",serif;color:var(--ink)}
.abs{position:absolute}
.top-strip{left:0;top:0;width:1084px;height:5px;background:var(--blue)}
.nav-band{left:0;top:5px;width:1084px;height:56px;background:var(--grey-band)}
.main-nav{left:195px;top:5px;height:56px;display:flex;font-family:"Roboto Condensed",sans-serif;font-weight:300;font-size:14px;color:#333}
.main-nav span{padding:0 13px;line-height:56px;border-right:1px solid #ddd}
.main-nav span:last-child{border-right:none}
.main-nav .active{background:var(--blue);color:#fff;padding:0 16px}
.brand{left:195px;top:78px;font-family:"Roboto Slab",serif;font-size:20px;color:var(--navy);letter-spacing:1px}
.header-contact{right:198px;top:72px;text-align:right;font-family:"Roboto Condensed",sans-serif;font-weight:300;font-size:13px;color:#444;line-height:22px}
.social{display:inline-flex;gap:5px;vertical-align:middle;margin-left:6px}
.social i{width:17px;height:17px;border-radius:2px;background:#3a67a8;display:block}
.social i:last-child{background:var(--blue)}
.hero{left:195px;top:126px;width:460px;height:298px;background:linear-gradient(180deg,#3a9ad6 0%,#7cc9ee 45%,#bfe3ec 62%,#e9dfc9 80%,#d9c9a8 100%)}
.dots{left:637px;top:370px;display:flex;flex-direction:column;gap:3px}
.dots i{width:8px;height:8px;background:#ccc;display:block}
.dots i:last-child{background:#fff}
.promo-list{left:655px;top:126px;width:231px;height:298px}
.promo{height:99.3px;border-bottom:1px solid #ddd;position:relative}
.promo:first-child{background:#f1f1f1}
.promo .thumb{position:absolute;left:17px;top:17px;width:65px;height:65px;border:3px solid #fff;box-shadow:0 0 0 1px #ccc}
.promo h4{position:absolute;left:93px;top:17px;font-family:"Roboto Condensed",sans-serif;font-weight:300;font-size:12.5px;color:#333}
.promo p{position:absolute;left:93px;top:34px;width:120px;font-family:"Roboto Condensed",sans-serif;font-weight:300;font-size:9px;line-height:13px;color:var(--blue)}
.promo b{position:absolute;left:198px;top:67px;width:14px;height:14px;background:var(--blue)}
.promo b:after{content:"";position:absolute;left:4px;top:5px;width:3px;height:3px;border-top:1px solid #fff;border-right:1px solid #fff;transform:rotate(45deg)}
.grey-section{left:0;top:424px;width:1084px;height:365px;background:linear-gradient(180deg,#e6e6e6,#fafafa)}
h2{font-family:"Roboto Slab",serif;font-weight:400;font-size:16px;color:var(--navy)}
.welcome-title{left:196px;top:443px}
.welcome-img{left:195px;top:474px;width:181px;height:120px;background:linear-gradient(180deg,#2d8fd3,#7cc7ea 60%,#3ea6c8)}
.welcome-text{left:388px;top:470px;width:262px;font-size:9px;line-height:14.5px;text-align:justify;color:#333}
.btn{background:linear-gradient(180deg,#1b7aa6,var(--navy));color:#fff;border-radius:5px;font-family:"Roboto Condensed",sans-serif;font-size:10px;text-align:center}
.read-more{left:583px;top:570px;width:66px;height:25px;line-height:25px}
.news-title{left:196px;top:629px}
.arrows{left:606px;top:636px;display:flex;gap:8px}
.arrows i{width:20px;height:20px;border-radius:50%;background:var(--navy);display:block}
.news-box{left:196px;top:662px;width:456px;height:116px;background:#dde3e3}
.news-img{left:208px;top:673px;width:114px;height:93px;background:linear-gradient(180deg,#6b7fa8,#c9d2df 55%,#5d8ab0)}
.news-text{left:373px;top:692px;width:272px;font-size:9px;line-height:14.5px;color:#333}
.news-text em{font-style:normal;color:#1e5fd0}
.search{left:672px;top:450px;width:214px;height:325px;background:var(--blue);color:#fff;font-family:"Roboto Condensed",sans-serif;font-size:9.5px}
.search h3{position:absolute;top:38px;width:100%;text-align:center;font-family:"Roboto Slab",serif;font-weight:300;font-size:15px}
.search label{position:absolute;line-height:12px}
.field{position:absolute;height:19px;background:#fff;border-radius:5px;color:#333;font-size:8.5px;line-height:19px;padding-left:10px}
.field.sel:after{content:"";position:absolute;right:0;top:0;width:19px;height:19px;background:var(--blue-dark);border-radius:0 5px 5px 0}
.submit{position:absolute;left:70px;top:274px;width:65px;height:25px;line-height:25px}
.numbers-title{left:194px;top:797px}
.sub{font-family:"Roboto Slab",serif;font-size:11px;color:#222}
.phone-list{left:195px;width:177px;font-size:9px;list-style:none}
.phone-list li{height:21.6px;line-height:20px;border-bottom:1px dotted #555;padding-left:20px;position:relative}
.phone-list li:last-child{border-bottom:none}
.phone-list svg{position:absolute;left:0;top:5px}
.photos-title{left:404px;top:797px}
.photo{top:829px;width:152px;height:125px;border:1px solid #ccc;padding:4px;background:#fff}
.photo div{width:100%;height:100%}
.members-title{left:405px;top:993px}
.badge{background:#e8eef2;border:1px solid #ccc}
.touch-title{left:672px;top:993px}
.touch-text{left:675px;top:1028px;width:212px;font-size:9px;line-height:14.5px}
.touch-list{left:673px;top:1073px;font-size:9px;line-height:21.6px;list-style:none}
.touch-list li{display:flex;align-items:center;gap:8px}
.touch-list span.ico{width:14px;height:12px;background:#b9c2c8;border-radius:2px}
.footer{left:0;top:1152px;width:1084px;height:48px;background:var(--footer)}
.footer-nav{left:195px;top:1169px;font-family:"Roboto Condensed",sans-serif;font-weight:300;font-size:9px;color:#fff;word-spacing:1px}
.copyright{right:198px;top:1169px;font-family:"Roboto Condensed",sans-serif;font-weight:300;font-size:9px;color:#fff}
</style>
</head>
<body>
<div class="abs top-strip"></div>
<div class="abs nav-band"></div>
<nav class="abs main-nav">
  <span class="active">Home</span><span>About us</span><span>Airfares</span><span>Hotels</span><span>Cars</span><span>Holidays</span><span>Cruises</span><span>Insurance</span><span>Contact Us</span>
</nav>

<div class="abs brand">VOYAGE HARBOUR</div>
<div class="abs header-contact">
  Phone No: (+612) 5550 1200<br>
  Follow Us: <span class="social"><i></i><i></i><i></i><i></i></span>
</div>

<div class="abs hero" role="img" aria-label="Woman reading in a hammock slung from a palm tree over a tropical beach"></div>
<div class="abs dots"><i></i><i></i><i></i><i></i></div>

<div class="abs promo-list">
  <div class="promo"><div class="thumb" role="img" aria-label="Cruise ship at sunset" style="background:linear-gradient(180deg,#d88a6a,#3b5a84)"></div><h4>Cruise</h4><p>Lorem Ipsum is simply dummy text of the printing.</p><b></b></div>
  <div class="promo"><div class="thumb" role="img" aria-label="Hiker in the mountains" style="background:linear-gradient(180deg,#8fa8bd,#4f5d4a)"></div><h4>Adventure</h4><p>Lorem Ipsum is simply dummy text.</p><b></b></div>
  <div class="promo"><div class="thumb" role="img" aria-label="Airliner in a blue sky" style="background:linear-gradient(180deg,#2f7dc4,#5aa3dc)"></div><h4>Flights</h4><p>Lorem Ipsum is simply dummy text ndustry.</p><b></b></div>
</div>

<div class="abs grey-section"></div>
<h2 class="abs welcome-title">Welcome to Voyage Harbour</h2>
<div class="abs welcome-img" role="img" aria-label="Hammock under palm trees by the sea"></div>
<p class="abs welcome-text">Lorem Ipsum is simply dummy text of the printing and typesetting industry. Lorem Ipsum has been the industry's standard dummy text ever since the 1500s, It has survived not only five centuries when an unknown printer took a galley of type and scrambled it to make a type specimen book. It has survived not only five centuries, but also the leap into electronic typesetting, remaining essentially unchanged.</p>
<div class="abs btn read-more">Read More</div>

<h2 class="abs news-title">Latest News &amp; Events</h2>
<div class="abs arrows"><i></i><i></i></div>
<div class="abs news-box"></div>
<div class="abs news-img" role="img" aria-label="River cruise boat by a town"></div>
<p class="abs news-text"><em>12:10:2012- Ipstum is simply dummy text of the printing</em> and typesetting industry. Lorem Ipsum has been the industry's standard dummy text ever not only five <em>centuries, but also the leap</em> the industry's standard dummy text ever since the 1500s,</p>

<form class="abs search">
  <h3>Quick Search</h3>
  <label style="left:27px;top:66px">Leaving from</label>
  <div class="field" style="left:27px;top:81px;width:161px"></div>
  <label style="left:27px;top:106px">Going to</label>
  <div class="field sel" style="left:27px;top:121px;width:161px">Kerala / moonnar</div>
  <label style="left:26px;top:148px">Adults</label><label style="left:76px;top:148px">Seniors</label><label style="left:136px;top:148px">Chield</label>
  <div class="field sel" style="left:26px;top:165px;width:48px;padding-left:5px">19-64</div>
  <div class="field sel" style="left:83px;top:165px;width:47px;padding-left:8px">65+</div>
  <div class="field sel" style="left:139px;top:165px;width:48px;padding-left:7px">0-18</div>
  <label style="left:27px;top:188px">Departing</label><label style="left:127px;top:188px">Time</label>
  <div class="field" style="left:27px;top:205px;width:92px"></div>
  <div class="field sel" style="left:127px;top:205px;width:60px;padding-left:20px">Any</div>
  <label style="left:27px;top:227px">Returning</label><label style="left:127px;top:227px">Time</label>
  <div class="field" style="left:27px;top:244px;width:92px"></div>
  <div class="field sel" style="left:127px;top:244px;width:60px;padding-left:20px">Any</div>
  <div class="btn submit">SUBMIT</div>
</form>

<h2 class="abs numbers-title">World wide Numbers</h2>
<div class="abs sub" style="left:196px;top:828px">Australian Phone Number</div>
<ul class="abs phone-list" style="top:845px">
  <li><svg width="8" height="10" viewBox="0 0 8 10"><path d="M4 0a4 4 0 0 1 4 4c0 3-4 6-4 6S0 7 0 4a4 4 0 0 1 4-4z" fill="#111"/><circle cx="4" cy="4" r="1.5" fill="#fff"/></svg>Sydney - &nbsp;(+612) 5550 1200</li>
  <li><svg width="8" height="10" viewBox="0 0 8 10"><path d="M4 0a4 4 0 0 1 4 4c0 3-4 6-4 6S0 7 0 4a4 4 0 0 1 4-4z" fill="#111"/><circle cx="4" cy="4" r="1.5" fill="#fff"/></svg>Adelaide - &nbsp;(+618) 5550 3471</li>
  <li><svg width="8" height="10" viewBox="0 0 8 10"><path d="M4 0a4 4 0 0 1 4 4c0 3-4 6-4 6S0 7 0 4a4 4 0 0 1 4-4z" fill="#111"/><circle cx="4" cy="4" r="1.5" fill="#fff"/></svg>Brisbane - &nbsp;(+617) 5550 8823</li>
  <li><svg width="8" height="10" viewBox="0 0 8 10"><path d="M4 0a4 4 0 0 1 4 4c0 3-4 6-4 6S0 7 0 4a4 4 0 0 1 4-4z" fill="#111"/><circle cx="4" cy="4" r="1.5" fill="#fff"/></svg>Canberra - &nbsp;(+612) 5550 6645</li>
  <li><svg width="8" height="10" viewBox="0 0 8 10"><path d="M4 0a4 4 0 0 1 4 4c0 3-4 6-4 6S0 7 0 4a4 4 0 0 1 4-4z" fill="#111"/><circle cx="4" cy="4" r="1.5" fill="#fff"/></svg>Melbourne - &nbsp;(+613) 5550 2290</li>
  <li><svg width="8" height="10" viewBox="0 0 8 10"><path d="M4 0a4 4 0 0 1 4 4c0 3-4 6-4 6S0 7 0 4a4 4 0 0 1 4-4z" fill="#111"/><circle cx="4" cy="4" r="1.5" fill="#fff"/></svg>Australia Wide FAX - (+612) 555</li>
</ul>
<div class="abs sub" style="left:195px;top:988px">International Phone Number</div>
<ul class="abs phone-list" style="top:1005px">
  <li><svg width="8" height="10" viewBox="0 0 8 10"><path d="M4 0a4 4 0 0 1 4 4c0 3-4 6-4 6S0 7 0 4a4 4 0 0 1 4-4z" fill="#111"/><circle cx="4" cy="4" r="1.5" fill="#fff"/></svg>&nbsp;Thailand - &nbsp;(+66) 55 501 204</li>
  <li><svg width="8" height="10" viewBox="0 0 8 10"><path d="M4 0a4 4 0 0 1 4 4c0 3-4 6-4 6S0 7 0 4a4 4 0 0 1 4-4z" fill="#111"/><circle cx="4" cy="4" r="1.5" fill="#fff"/></svg>&nbsp;Thailand FAX - (+66) 55 502 658</li>
  <li><svg width="8" height="10" viewBox="0 0 8 10"><path d="M4 0a4 4 0 0 1 4 4c0 3-4 6-4 6S0 7 0 4a4 4 0 0 1 4-4z" fill="#111"/><circle cx="4" cy="4" r="1.5" fill="#fff"/></svg>&nbsp;Bangkok - &nbsp;(+66) 2 5550164</li>
  <li><svg width="8" height="10" viewBox="0 0 8 10"><path d="M4 0a4 4 0 0 1 4 4c0 3-4 6-4 6S0 7 0 4a4 4 0 0 1 4-4z" fill="#111"/><circle cx="4" cy="4" r="1.5" fill="#fff"/></svg>&nbsp;Hong Kong - &nbsp;(+852) 5550 2158</li>
  <li><svg width="8" height="10" viewBox="0 0 8 10"><path d="M4 0a4 4 0 0 1 4 4c0 3-4 6-4 6S0 7 0 4a4 4 0 0 1 4-4z" fill="#111"/><circle cx="4" cy="4" r="1.5" fill="#fff"/></svg>&nbsp;USA - &nbsp;(+1) 213 555 0143</li>
  <li><svg width="8" height="10" viewBox="0 0 8 10"><path d="M4 0a4 4 0 0 1 4 4c0 3-4 6-4 6S0 7 0 4a4 4 0 0 1 4-4z" fill="#111"/><circle cx="4" cy="4" r="1.5" fill="#fff"/></svg>&nbsp;UK - &nbsp;(+44) 208 555 0770</li>
</ul>

<h2 class="abs photos-title">Featured Traveller Photos</h2>
<div class="abs photo" style="left:401px"><div role="img" aria-label="Canal street with old buildings at dusk" style="background:linear-gradient(180deg,#4a4a52,#7a5a48 60%,#2d2a2a)"></div></div>
<div class="abs photo" style="left:568px"><div role="img" aria-label="Waterfall in a green forest" style="background:linear-gradient(180deg,#2f5a2a,#6f9a6a 55%,#6fb6c0)"></div></div>
<div class="abs photo" style="left:735px"><div role="img" aria-label="City park fountain with skyline" style="background:linear-gradient(180deg,#8fb8e0,#a0a8a8 50%,#5f7a4a)"></div></div>

<h2 class="abs members-title">We are Members Of</h2>
<div class="abs badge" style="left:405px;top:1058px;width:46px;height:33px"></div>
<div class="abs badge" style="left:458px;top:1040px;width:130px;height:100px"></div>
<div class="abs badge" style="left:595px;top:1058px;width:47px;height:33px"></div>

<h2 class="abs touch-title">Get in Touch</h2>
<p class="abs touch-text">Lorem Ipsum is simply dummy text of the printing and typesetting industry. Lorem Ipsum. text of the printing..</p>
<ul class="abs touch-list">
  <li><span class="ico"></span>: &nbsp;(+612) 5550 1200</li>
  <li><span class="ico"></span>: (+612) 555 200 78</li>
  <li><span class="ico"></span>: sales @ voyageharbour-example.com.au</li>
</ul>

<div class="abs footer"></div>
<div class="abs footer-nav">Home &nbsp;| &nbsp;&nbsp;About us &nbsp;&nbsp;| &nbsp;&nbsp;Airfares &nbsp;| &nbsp;&nbsp;Hotels &nbsp;| &nbsp;&nbsp;Cars &nbsp;| &nbsp;&nbsp;Holidays &nbsp;&nbsp;| &nbsp;&nbsp;Cruises &nbsp;| &nbsp;&nbsp;Insurance &nbsp;| &nbsp;&nbsp;Contact Us</div>
<div class="abs copyright">2012@All Rights Reserved.</div>
</body>
</html>
```